THE PRACTICE NAME "The Corvane MD" FOR A NEW MEDICAL PRACTICE STARTUP

THIS IS A BUSINESS CARD REQUEST FOR A KIDNEY DOCTOR's(NEPHROLOGIST) PRACTICE, THIS PRACTICE WILL BE IN EL PASO,TEXAS USA.OPEN TO INNOVATIVE IDEAS!

THE CORVANE MD ( NAME OF PRACTICE)

DEVESH R. MALHOTRA, MD FNKF FASN ( NAME OF PHYSICIAN WITH DEGREES)
BOARD CERTIFIED INTERNAL MEDICINE
BOARD CERTIFIED NEPHROLOGY
HYPERTENSION SPECIALIST

OFFICE ADDRESS, PHONE, FAX AND EMAIL PENDING

Saving Kidneys. Saving Lives.(MOTTO) THE LOGO SHOILD REFLECT THIS MESSAGE. WE NEED A LOGO DESIGN WITH 2 KIDNEYS OR CAN BE ONE KIDNEY ALSO.

Target Market(s)

PATIENTS WITH KIDNEY DISEASE, HYPERTENSION, ENGLISH AND SPANISH SPEAKING POPULATION AND PATIENTS ON DIALYSIS

Industry/Entity Type

Health Care

Contact Information for Business Card

HYPERTENSION SPECIALIST

WEBSITE URL PENDING

Font styles to use
Serif
Sans Serif
Script

Colors
fbed38
ffc214
fbf289
fbee3e
5c5c5c
333333
1b1b1b
757575
d3d3d3

Requirements
Must have
• A KIDNEY LOGO
• NAME OF THE PRACTICE
Nice to have
• IF THE CARD CAN BE IN THE SHAPE OF A KIDNEY

```html
<!DOCTYPE html>
<html lang="en">
<head>
<meta charset="utf-8">
<title>The Corvane MD – Business Card</title>
<link href="https://fonts.googleapis.com/css2?family=Source+Sans+3:wght@400;600;700&display=swap" rel="stylesheet">
<style>
  :root {
    --page-bg: #e4e1dc;
    --card-white: #ffffff;
    --silver-light: #f4f4f4;
    --silver-mid: #d3d3d3;
    --maroon: #5a1014;
    --maroon-dark: #3f0a0d;
    --gold: #ffc214;
    --ink: #1b1b1b;
    --ink-soft: #333333;
  }
  * { box-sizing: border-box; margin: 0; padding: 0; }
  html, body {
    width: 1200px; height: 900px; overflow: hidden;
    background: var(--page-bg);
    font-family: "Source Sans 3", "Helvetica Neue", Arial, sans-serif;
  }
  .card {
    position: absolute; left: 150px; top: 200px;
    width: 900px; height: 500px;
    border-radius: 40px; overflow: hidden;
    background: var(--card-white);
    box-shadow: 0 10px 30px rgba(0,0,0,.25);
  }
  .card-header {
    height: 150px;
    background: linear-gradient(180deg, var(--silver-light) 0%, #e2e2e2 100%);
    border-bottom: 3px solid var(--silver-mid);
    display: flex; align-items: center; padding-left: 70px;
  }
  .practice-name {
    font-weight: 600; font-size: 52px;
    color: var(--ink);
  }
  .card-body {
    display: flex; justify-content: space-between;
    padding: 22px 60px 0 60px;
  }
  .contact-list { list-style: none; color: var(--ink); font-size: 23px; line-height: 1.15; }
  .contact-list li { display: flex; align-items: flex-start; gap: 20px; margin-bottom: 3px; }
  .contact-list .address { margin-bottom: 8px; }
  .icon { width: 22px; height: 22px; flex: none; margin-top: 3px; fill: var(--maroon-dark); }
  .physician { text-align: right; color: var(--ink-soft); padding-top: 14px; }
  .physician-name { font-weight: 700; font-size: 25px; color: var(--ink); margin-bottom: 4px; }
  .physician-role { font-size: 22px; line-height: 1.2; }
  .motto-band {
    position: absolute; left: 0; bottom: 0; width: 100%; height: 90px;
    background: linear-gradient(180deg, var(--maroon) 0%, var(--maroon-dark) 100%);
    display: flex; align-items: center; padding-left: 100px;
  }
  .motto { color: var(--gold); font-weight: 700; font-size: 44px; letter-spacing: .5px; }
</style>
</head>
<body>
  <section class="card">
    <header class="card-header">
      <p class="practice-name">The Corvane MD</p>
    </header>

    <div class="card-body">
      <ul class="contact-list">
        <li class="address">
          <svg class="icon" viewBox="0 0 24 24"><path d="M12 1a8 8 0 0 0-8 8c0 6 8 14 8 14s8-8 8-14a8 8 0 0 0-8-8zm0 11a3 3 0 1 1 0-6 3 3 0 0 1 0 6z"/></svg>
          <span>4520 N. Mesa Vista Blvd.<br>Suite 208, PMB 310<br>El Paso, TX 79912</span>
        </li>
        <li>
          <svg class="icon" viewBox="0 0 24 24"><path d="M6.6 10.8a15 15 0 0 0 6.6 6.6l2.2-2.2c.3-.3.7-.4 1-.2 1.1.4 2.3.6 3.6.6.6 0 1 .4 1 1V20c0 .6-.4 1-1 1A17 17 0 0 1 3 4c0-.6.4-1 1-1h3.5c.6 0 1 .4 1 1 0 1.3.2 2.5.6 3.6.1.3 0 .7-.2 1z"/></svg>
          <span>915.555.0142</span>
        </li>
        <li>
          <svg class="icon" viewBox="0 0 24 24"><path d="M7 2h8v6H7zM3 9h18v11H3zm3 3v2h2v-2zm4 0v2h2v-2zm4 0v2h4v-2zM6 16v2h2v-2zm4 0v2h2v-2z"/></svg>
          <span>915.555.0143</span>
        </li>
        <li>
          <svg class="icon" viewBox="0 0 24 24"><path d="M2 5h20v14H2zm2 2v.5l8 5.5 8-5.5V7l-8 5.3z"/></svg>
          <span>devesh@corvanemd.com</span>
        </li>
        <li>
          <svg class="icon" viewBox="0 0 24 24"><path d="M12 2a10 10 0 1 0 0 20 10 10 0 0 0 0-20zm0 2c.9 1 1.7 2.5 2.1 4H9.9C10.3 6.5 11.1 5 12 4zM4.3 14a8 8 0 0 1 0-4h3.3a14 14 0 0 0 0 4zm1 2h2.9c.4 1.4.9 2.6 1.6 3.6A8 8 0 0 1 5.3 16zm2.9-8H5.3a8 8 0 0 1 4.5-3.6C9.1 5.4 8.6 6.6 8.2 8zM12 20c-.9-1-1.7-2.5-2.1-4h4.2c-.4 1.5-1.2 3-2.1 4zm2.4-6H9.6a12 12 0 0 1 0-4h4.8a12 12 0 0 1 0 4zm-.2 5.6c.7-1 1.2-2.2 1.6-3.6h2.9a8 8 0 0 1-4.5 3.6zm2.2-5.6a14 14 0 0 0 0-4h3.3a8 8 0 0 1 0 4z"/></svg>
          <span>www.corvanemd.com</span>
        </li>
      </ul>

      <div class="physician">
        <p class="physician-name">Devesh R. Malhotra, MD FNKF FASN</p>
        <p class="physician-role">Board Certified Internal Medicine</p>
        <p class="physician-role">Board Certified Nephrology</p>
        <p class="physician-role">Hypertension Specialist</p>
      </div>
    </div>

    <footer class="motto-band">
      <p class="motto">Saving Kidneys. Saving Lives</p>
    </footer>
  </section>
</body>
</html>
```